Flier Template in Microsoft Word

We need to a have a flier about farm practices developed in Microsoft Word. Each farm will able to add their own logos and photos. We will give them a model that they can customize.

We want a traditional "country" flavor. Green colors and earth tones are best. Please use the photos we have provided.

The final product must be in Microsoft Word for our farmers to customize.
Updates

All designers: Please have a white background (maybe with a watermark). Our client will print these on white paper using a desktop printer. Thank you!

Target Market(s)

People who shop at Farmer's Markets, join CSAs, and enjoy cooking with fresh vegetables.

Industry/Entity Type

Farm

Font styles to use
Serif

Requirements
Must have
• Must use the text and general layout of the Microsoft Word document attached
Must use the pictures we provided.
Final product must be in Microsoft Word
Must be able to easily swap out the logo at the top
Must be able to print on white paper on a desktop printer
Nice to have
• A nice header that looks like a farm or food on the table
A nice watermark or background to make the flier look polished
Should not have
• Do not change the photos
Do not use high tech fonts or graphic treatments

```html
<!DOCTYPE html>
<html lang="en">
<head>
<meta charset="utf-8">
<title>Sustainable Grazing Flier</title>
<link rel="stylesheet" href="https://fonts.googleapis.com/css2?family=Carlito:wght@400;700&display=swap">
<style>
  :root {
    --backdrop: #e9e6e1;
    --paper: #ffffff;
    --brown: #8a4516;
    --green: #1e9a1e;
    --logo-green: #16a02a;
    --lime: #8cc63f;
    --ink: #3b3b3b;
    --band-ink: #1d3a12;
  }
  * { box-sizing: border-box; margin: 0; padding: 0; }
  html, body { width: 1200px; height: 831px; overflow: hidden; background: var(--backdrop); }
  body { font-family: "Carlito", "Calibri", sans-serif; color: var(--ink); }

  .stage {
    width: 1040px; height: 720px; position: relative;
    transform: scale(1.15385); transform-origin: 0 0;
  }
  .page {
    position: absolute; top: 50px; width: 461px; height: 642px;
    background: var(--paper); box-shadow: 0 1px 4px rgba(0,0,0,.18);
  }
  .page--story { left: 44px; }
  .page--impact { left: 535px; }
  .page > * { position: absolute; }

  .logo { left: 20px; top: 26px; font-size: 18px; color: var(--logo-green); letter-spacing: .3px; }
  .header-photo {
    left: 149px; top: 0; width: 310px; height: 83px;
    background: linear-gradient(180deg, #e8f1f6 0%, #dfeaf0 32%, #7aa24a 42%, #4f4a3f 62%, #7fa83e 80%, #9cbc4a 100%);
  }

  .title { left: 0; width: 461px; top: 91px; text-align: center; font-size: 16px; font-weight: 700; color: var(--brown); letter-spacing: .3px; }
  .subtitle { left: 0; width: 461px; top: 113px; text-align: center; font-size: 11px; font-weight: 700; color: var(--green); }

  .heading { left: 42px; font-size: 13px; font-weight: 700; color: var(--brown); letter-spacing: .2px; }
  .copy { left: 42px; font-size: 9.6px; line-height: 14.6px; }
  .copy--small { font-size: 7.7px; line-height: 12px; width: 378px; }

  .photo { box-shadow: 0 1px 3px rgba(0,0,0,.3); }
  .photo--farmer { left: 251px; top: 135px; width: 167px; height: 111px;
    background: linear-gradient(180deg, #b9cbd6 0%, #6f8f4e 38%, #4c7a2c 70%, #6c9a3c 100%); }
  .photo--before { left: 42px; top: 432px; width: 182px; height: 124px;
    background: linear-gradient(180deg, #a9c6e4 0%, #8b8a7a 30%, #6f7d4a 55%, #8b7a62 100%); }
  .photo--after { left: 238px; top: 432px; width: 180px; height: 124px;
    background: linear-gradient(180deg, #9fc3e6 0%, #7a8f78 30%, #6d9a3a 60%, #8a9a3c 100%); }

  .partner-badge { left: 44px; top: 576px; width: 64px; height: 54px; }
  .partner-note { left: 118px; top: 583px; width: 310px; font-size: 8.6px; line-height: 13px; color: #222; }

  .compare-band { left: 0; top: 89px; width: 461px; height: 27px; background: var(--green); }
  .compare-band span { position: absolute; top: 6px; font-size: 13px; font-weight: 700; color: var(--band-ink); transform: translateX(-50%); }
  .compare-band .before { left: 115px; }
  .compare-band .after { left: 331px; }

  .card { width: 172px; }
  .card .photo { width: 100%; }
  .card .caption {
    background: var(--lime); color: #1e2a10; font-size: 8.6px; line-height: 13px;
    text-align: center; padding: 3px 6px;
  }
  .card--market { left: 43px; top: 191px; }
  .card--market .photo { height: 129px; background: linear-gradient(160deg, #7f9a6a 0%, #c7a14a 40%, #c5473a 65%, #6b7a3a 100%); }
  .card--market .caption { height: 48px; }
  .card--kitchen { left: 247px; top: 191px; width: 171px; }
  .card--kitchen .photo { height: 131px; background: linear-gradient(160deg, #f2ede4 0%, #d9c2a6 45%, #8fb04a 75%, #d94a2a 100%); }
  .card--kitchen .caption { height: 46px; padding-top: 5px; }
  .card--fishing { left: 43px; top: 385px; }
  .card--fishing .photo { height: 130px; background: linear-gradient(180deg, #c9dde6 0%, #6f8fa3 40%, #5a4a3c 70%, #3e5a7a 100%); }
  .card--fishing .caption { height: 55px; }
  .card--osprey { left: 247px; top: 385px; width: 171px; }
  .card--osprey .photo { height: 130px; background: linear-gradient(180deg, #3e3a2a 0%, #6b5a3c 45%, #8a7a5a 75%, #4a4a3a 100%); }
  .card--osprey .caption { height: 55px; padding-top: 5px; }
</style>
</head>
<body>
<div class="stage">

  <section class="page page--story">
    <div class="logo">YOUR LOGO</div>
    <div class="header-photo" role="img" aria-label="Herd of dairy cows grazing in a green pasture with red barns behind"></div>

    <h1 class="title">SUSTAINABLE GRAZING</h1>
    <p class="subtitle">Happier Cows = Healthier Milk and Cleaner Streams</p>

    <h2 class="heading" style="top:137px">WHO WE ARE</h2>
    <p class="copy" style="top:157px;width:198px">Millbrook Dairy Farm is a third generation dairy farm located on 64 acres in the Harlow Valley.&nbsp; We raise Holsteins to produce milk and also raise hens for eggs.&nbsp; We sell much of our milk, as well as&nbsp; cheese, yogurt and baked goods directly from the farm.</p>
    <div class="photo photo--farmer" role="img" aria-label="Farmer standing in front of a red tractor in a green field"></div>

    <h2 class="heading" style="top:254px">WHAT HAVE WE DONE</h2>
    <p class="copy copy--small" style="top:271px">At Millbrook Dairy Farm, we take care of our animals and our animals help us take care of the land.&nbsp; Corn and other grains are not a natural part of a cows' diet, so we don't feed them that.&nbsp; Instead, we let them roam the pastures eating grass and other plants.&nbsp; We move the cows from pasture to pasture on a thoughtful schedule to prevent overgrazing, and this reduces soil erosion and water pollution.&nbsp; Our animals are happier and our land and water is healthier.</p>

    <h2 class="heading" style="top:348px">WHEN AND WHERE WE DID IT</h2>
    <p class="copy copy--small" style="top:365px">In 2010, we had our cows in a stall barn and corn or soybeans in our fields.&nbsp; We looked into switching some of our acreage from crops to pasture and soon realized that it would beneficial to our cows and our soil.&nbsp; We then installed fencing to divide the fields into smaller paddocks and in spring 2011, we planted a seed mixture containing plants that provide the nutrition our cows need and that provides support for the soil.</p>

    <div class="photo photo--before" role="img" aria-label="Pasture with cattle beside an eroded stream before improvements"></div>
    <div class="photo photo--after" role="img" aria-label="Fenced stream with healthy green banks after improvements"></div>

    <svg class="partner-badge" viewBox="0 0 64 54" aria-hidden="true"><circle cx="30" cy="27" r="24" fill="#a8d86a"/></svg>
    <p class="partner-note">Riverside RC &amp; D's growing promotes local farms that produce fresh, high quality, healthy environmental farm practices that keep our water clean and our families safe.</p>
  </section>

  <section class="page page--impact">
    <div class="logo">YOUR LOGO</div>
    <div class="header-photo" role="img" aria-label="Herd of dairy cows grazing in a green pasture with red barns behind"></div>

    <div class="compare-band"><span class="before">BEFORE</span><span class="after">AFTER</span></div>

    <h2 class="heading" style="top:126px;left:43px">WHY YOU SHOULD CARE</h2>
    <p class="copy" style="top:141px;left:43px;width:380px">Millbrook Dairy Farm is a third generation dairy farm located on 64 acres in the Harlow Valley.&nbsp; We raise Holsteins to produce milk and also raise hens for eggs.&nbsp; We sell much of our milk, as well as cheese, yogurt and baked goods directly from the farm.</p>

    <div class="card card--market">
      <div class="photo" role="img" aria-label="Farmers market stall with fresh fruit and vegetables"></div>
      <p class="caption">Fresh and locally produced food from our farm tastes better, and it's better for our local economy and environment.</p>
    </div>
    <div class="card card--kitchen">
      <div class="photo" role="img" aria-label="Mother and daughter enjoying fresh vegetables in a kitchen"></div>
      <p class="caption">Fresh food is healthier for kids of all ages than processed food.</p>
    </div>
    <div class="card card--fishing">
      <div class="photo" role="img" aria-label="Family holding a fish they caught by a river"></div>
      <p class="caption">As a result of the improvements described here, the waterways that run through our farm are cleaner, benefitting everyone downstream.</p>
    </div>
    <div class="card card--osprey">
      <div class="photo" role="img" aria-label="Osprey lifting off from the water with a catch"></div>
      <p class="caption">Our wildlife neighbours appreciate the cleaner waterways even more than you do!</p>
    </div>

    <svg class="partner-badge" viewBox="0 0 64 54" aria-hidden="true"><circle cx="30" cy="27" r="24" fill="#a8d86a"/></svg>
    <p class="partner-note">Riverside RC &amp; D's growing promotes local farms that produce fresh, high quality, healthy environmental farm practices that keep our water clean and our families safe.</p>
  </section>

</div>
</body>
</html>
```